Business Card Colourful and fun Design Project

I need a business card design for my Ecommerce website which am launching soon. we are based in the United Arab Emirates and our customers are based in Dubai and other cities in UAE, In addition to our neighbour countries in the GCC. We sell Gadgets, fashion and other trendy stuff that are hard to find in our market. The company name is "ZIPKOALA" logo consists of a panda wearing traditional local Arab thobe. would like to see a clean, colourful fun design to represent us.
Updates
please read the discussion board. thanks
Industry/Entity Type
Fashion
Look and feel
Each slider illustrates characteristics of the customer's brand and the style your logo design should communicate.

```html
<!DOCTYPE html>
<html lang="en">
<head>
<meta charset="utf-8">
<title>ZIPKOALA Business Card</title>
<link rel="stylesheet" href="https://fonts.googleapis.com/css2?family=Questrial&display=swap">
<style>
  :root {
    --stage: #2a2a2c;
    --brand-red: #b5141f;
    --deep-red: #8f0f18;
    --ink: #1c1c1e;
    --paper: #e9eaee;
    --mascot-light: #d9dadd;
    --mascot-shade: #a9abb0;
  }
  * { box-sizing: border-box; margin: 0; padding: 0; }
  html, body {
    width: 1200px; height: 900px; overflow: hidden;
    background: var(--stage);
    font-family: "Questrial", sans-serif;
  }
  .stage {
    position: relative; width: 1200px; height: 900px;
    display: flex; align-items: center; justify-content: center; gap: 60px;
  }
  .card {
    position: relative; width: 520px; height: 300px; overflow: hidden;
    box-shadow: 0 14px 30px rgba(0,0,0,.45);
  }

  /* Front */
  .card-front { background: var(--ink); }
  .front-pattern {
    position: absolute; inset: 0;
    background: linear-gradient(135deg, var(--deep-red) 0%, var(--brand-red) 40%, #3a1014 75%, var(--ink) 100%);
  }
  .front-mascot {
    position: absolute; left: 0; top: 0; width: 250px; height: 210px;
    background: radial-gradient(ellipse at 50% 40%, #f4f4f6 0%, var(--mascot-light) 55%, var(--mascot-shade) 100%);
    border-bottom-right-radius: 110px;
  }
  .front-brand {
    position: absolute; left: 150px; bottom: 34px;
    font-size: 64px; letter-spacing: 2px; color: var(--brand-red);
    background: #fff; padding: 2px 14px; line-height: 1.1;
  }

  /* Back */
  .card-back { background: var(--paper); color: var(--ink); }
  .back-mascot {
    position: absolute; left: 26px; top: 26px; width: 82px; height: 112px;
    border-radius: 40px 40px 12px 12px;
    background: linear-gradient(180deg, var(--mascot-light), var(--mascot-shade));
  }
  .back-brand {
    position: absolute; left: 118px; top: 80px;
    font-size: 46px; letter-spacing: 2px; color: var(--brand-red);
  }
  .holder { position: absolute; left: 74px; top: 152px; }
  .holder-name { font-size: 20px; color: var(--brand-red); letter-spacing: 1px; }
  .holder-role { font-size: 13px; margin-top: 3px; }
  .address {
    position: absolute; left: 74px; top: 210px;
    font-size: 13px; line-height: 1.55; font-style: normal;
  }
  .contact {
    position: absolute; left: 290px; top: 226px;
    font-size: 13px; line-height: 1.6; list-style: none;
  }
  .contact-label { color: var(--brand-red); }
</style>
</head>
<body>
<main class="stage">
  <section class="card card-front">
    <div class="front-pattern" role="img" aria-label="Decorative pattern of scattered red, white and black squares"></div>
    <div class="front-mascot" role="img" aria-label="Mascot illustration: panda wearing a traditional thobe and headscarf, arms crossed"></div>
    <p class="front-brand">ZIPKOALA</p>
  </section>

  <section class="card card-back">
    <div class="back-mascot" role="img" aria-label="Small mascot illustration: panda in a traditional thobe"></div>
    <p class="back-brand">ZIPKOALA</p>
    <div class="holder">
      <p class="holder-name">LENA MARLOW</p>
      <p class="holder-role">Sales Manager</p>
    </div>
    <address class="address">
      Address 48 Ka, 5120 Dereli<br>
      Cinar Sk 67890 Ordu
    </address>
    <ul class="contact">
      <li><span class="contact-label">PHONE:</span> + 35 555 0194</li>
      <li><span class="contact-label">EMAIL:</span> lena@zipkoala.com</li>
    </ul>
  </section>
</main>
</body>
</html>
```